Core Values Poster for Healthcare company

Trying to Create a core values poster for my company. Healthcare Company - We have Neurosurgery, Pain Management, Physical Therapy, Occupational Therapy, Rehab, Imaging, and psychology so far and we are growing fast.

Core Values would Include - (Execution), (Loyalty), (Innovation), (Synergy), (Growth-Oriented), (Ethics & Integrity), (Love), and (Energy)

Please incorporate the Company Logo which is on the website and I have included it in my uploads. As long as the logo stays blue it does not need a gradient effect.

I like the posters made for this contest : https://quillvane.com.au/poster-design/contests/make-team-principles-wallchart-815327

This picture should be memorable so people know our Core Values

Target Market(s)

Staff in the company

Colors

Designer to choose colors to be used in the design.

Requirements
Must have
• Logo
Nice to have
• Pictures for each core value

```html
<!DOCTYPE html>
<html lang="en">
<head>
<meta charset="utf-8">
<title>Brightvale Core Values</title>
<link rel="stylesheet" href="https://fonts.googleapis.com/css2?family=Libre+Baskerville&family=Montserrat:wght@500&display=swap">
<style>
  :root {
    --brand-blue: #1f8dc5;
    --ribbon-dark: #333333;
    --paper: #ffffff;
    --loyalty: #6b449c;
    --innovation: #f9d035;
    --synergy: #4fc2b7;
    --growth: #4caf50;
    --ethics: #f7932f;
    --love-energy: #e2312b;
    --execution: #4fc3ef;
    --icon-white: #ffffff;
  }
  html, body {
    margin: 0;
    padding: 0;
    width: 1200px;
    height: 1138px;
    overflow: hidden;
    background: var(--paper);
  }
  .poster {
    position: relative;
    width: 1200px;
    height: 1138px;
    font-family: "Libre Baskerville", Georgia, serif;
  }
  .brand {
    position: absolute;
    top: 66px;
    left: 0;
    width: 100%;
    display: flex;
    justify-content: center;
    align-items: center;
    gap: 20px;
  }
  .brand-square {
    width: 70px;
    height: 70px;
    border-radius: 6px;
    background: var(--brand-blue);
  }
  .brand-name {
    font-size: 72px;
    line-height: 1;
    color: var(--brand-blue);
    letter-spacing: 2px;
  }
  .ribbon {
    position: absolute;
    top: 200px;
    left: 365px;
    width: 470px;
    height: 60px;
  }
  .ribbon-title {
    position: absolute;
    top: 200px;
    left: 0;
    width: 100%;
    height: 60px;
    line-height: 60px;
    text-align: center;
    color: var(--paper);
    font-size: 34px;
    letter-spacing: 1px;
  }
  .values-wheel {
    position: absolute;
    top: 0;
    left: 0;
  }
  .value-label {
    font-family: "Montserrat", Arial, sans-serif;
    font-weight: 500;
    font-size: 27px;
    text-anchor: middle;
  }
  .footer-link {
    position: absolute;
    top: 1052px;
    left: 0;
    width: 100%;
    text-align: center;
    color: var(--brand-blue);
    font-size: 28px;
  }
</style>
</head>
<body>
<main class="poster">
  <header class="brand">
    <span class="brand-square"></span>
    <span class="brand-name">BRIGHTVALE</span>
  </header>

  <svg class="ribbon" viewBox="0 0 470 60" aria-hidden="true">
    <polygon points="0,0 470,0 450,30 470,60 0,60 20,30" fill="var(--ribbon-dark)"/>
  </svg>
  <h1 class="ribbon-title" style="margin:0;font-weight:400;">CORE VALUES</h1>

  <svg class="values-wheel" width="1200" height="1138" viewBox="0 0 1200 1138">
    <defs>
      <polygon id="value-slice" points="0,35 -135,300 135,300" stroke-width="22" stroke-linejoin="round"/>
    </defs>

    <g class="wheel-slices" transform="translate(600 641)">
      <use href="#value-slice" fill="var(--ethics)" stroke="var(--ethics)" transform="rotate(0)"/>
      <use href="#value-slice" fill="var(--love-energy)" stroke="var(--love-energy)" transform="rotate(51.43)"/>
      <use href="#value-slice" fill="var(--execution)" stroke="var(--execution)" transform="rotate(102.86)"/>
      <use href="#value-slice" fill="var(--loyalty)" stroke="var(--loyalty)" transform="rotate(154.29)"/>
      <use href="#value-slice" fill="var(--innovation)" stroke="var(--innovation)" transform="rotate(205.71)"/>
      <use href="#value-slice" fill="var(--synergy)" stroke="var(--synergy)" transform="rotate(257.14)"/>
      <use href="#value-slice" fill="var(--growth)" stroke="var(--growth)" transform="rotate(308.57)"/>
    </g>

    <!-- Execution: target -->
    <g class="icon-target" fill="none" stroke="var(--icon-white)" stroke-width="8">
      <circle cx="400" cy="600" r="40"/>
      <circle cx="400" cy="600" r="22"/>
      <circle cx="400" cy="600" r="6" fill="var(--icon-white)"/>
      <line x1="400" y1="600" x2="452" y2="600" stroke-linecap="round"/>
      <path d="M440 588 L452 600 L440 612" stroke-linecap="round" stroke-linejoin="round"/>
    </g>

    <!-- Loyalty: artwork area -->
    <circle cx="513" cy="465" r="44" fill="var(--icon-white)" opacity="0.35" role="img" aria-label="Lotus flower held in open hands"/>

    <!-- Innovation: light bulb -->
    <g class="icon-bulb" stroke="var(--icon-white)" stroke-width="7" stroke-linecap="round" fill="none">
      <circle cx="687" cy="452" r="24"/>
      <path d="M676 474 L676 490 L698 490 L698 474"/>
      <line x1="678" y1="500" x2="696" y2="500"/>
      <line x1="687" y1="410" x2="687" y2="400"/>
      <line x1="652" y1="424" x2="645" y2="417"/>
      <line x1="722" y1="424" x2="729" y2="417"/>
      <line x1="640" y1="454" x2="630" y2="454"/>
      <line x1="734" y1="454" x2="744" y2="454"/>
    </g>

    <!-- Synergy: artwork area -->
    <circle cx="795" cy="596" r="44" fill="var(--icon-white)" opacity="0.35" role="img" aria-label="Three people joined in a circle"/>

    <!-- Growth-Oriented: artwork area -->
    <circle cx="756" cy="766" r="44" fill="var(--icon-white)" opacity="0.35" role="img" aria-label="Young plant growing from an open hand"/>

    <!-- Ethics & Integrity: scales -->
    <g class="icon-scales" stroke="var(--icon-white)" stroke-width="7" stroke-linecap="round" fill="none">
      <line x1="600" y1="800" x2="600" y2="872"/>
      <line x1="578" y1="874" x2="622" y2="874"/>
      <line x1="556" y1="812" x2="644" y2="812"/>
      <path d="M556 812 L540 846 L572 846 Z" stroke-linejoin="round"/>
      <path d="M644 812 L628 846 L660 846 Z" stroke-linejoin="round"/>
    </g>

    <!-- Love, and Energy: heart -->
    <g class="icon-heart">
      <path d="M444 790 C412 766 404 748 416 735 C428 723 440 730 444 740 C448 730 460 723 472 735 C484 748 476 766 444 790 Z" fill="var(--icon-white)"/>
      <g stroke="var(--icon-white)" stroke-width="6" stroke-linecap="round">
        <line x1="444" y1="714" x2="444" y2="704"/>
        <line x1="412" y1="722" x2="405" y2="715"/>
        <line x1="476" y1="722" x2="483" y2="715"/>
      </g>
    </g>

    <text class="value-label" fill="var(--loyalty)" transform="translate(458 346) rotate(-25.7)">Loyalty</text>
    <text class="value-label" fill="var(--innovation)" transform="translate(742 346) rotate(25.7)">Innovation</text>
    <text class="value-label" fill="var(--synergy)" transform="translate(920 568) rotate(77.1)">Synergy</text>
    <text class="value-label" fill="var(--execution)" transform="translate(280 568) rotate(-77.1)">Execution</text>
    <text class="value-label" fill="var(--growth)" transform="translate(878 862) rotate(-51.4)">Growth-Oriented</text>
    <text class="value-label" fill="var(--love-energy)" transform="translate(322 862) rotate(51.4)">Love, and Energy</text>
    <text class="value-label" fill="var(--ethics)" transform="translate(600 996)">Ethics &amp; Integrity</text>
  </svg>

  <footer class="footer-link">For more information visit www.brvl.com</footer>
</main>
</body>
</html>
```